Consultancy company needs flyer design

We need a flyer design for a new service to be provided. It is a service in which project management is outsourced. Text of the service has been attached (in Dutch).
We would like the design to be in line with our website design (www.veltoris.com). Also we would like to re-use the main banner of the site (see attachment)

Industry/Entity Type

It Company

Requirements
Must have
• Flyer must be double sided

```html
<!DOCTYPE html>
<html lang="nl">
<head>
<meta charset="utf-8">
<title>Veltoris – PMAAS flyer</title>
<link href="https://fonts.googleapis.com/css2?family=Ubuntu:wght@400;500;700&family=Open+Sans:wght@400;600;700&family=Roboto+Condensed:wght@700&display=swap" rel="stylesheet">
<style>
  :root{
    --teal:#3a86a3;
    --teal-dark:#2c6f8a;
    --orange:#d6862a;
    --paper:#ffffff;
    --paper-soft:#eef0f1;
    --ink:#1c1c1c;
    --stage:#5b5d60;
    --white:#ffffff;
  }
  *{box-sizing:border-box;margin:0;padding:0}
  html,body{width:1200px;height:1200px;overflow:hidden;background:var(--stage)}
  .canvas{position:relative;width:1200px;height:1200px}
  .flyer{position:absolute;top:221px;width:540px;height:758px;overflow:hidden;background:var(--paper);
    box-shadow:0 6px 18px rgba(0,0,0,.35);font-family:"Open Sans",sans-serif;color:var(--ink)}
  .flyer--front{left:30px}
  .flyer--back{left:630px;background:var(--paper-soft)}
  .shapes{position:absolute;inset:0;width:540px;height:758px}
  .abs{position:absolute}

  /* front */
  .front-header{left:0;top:0;width:540px;height:97px;background:var(--teal);color:var(--white);
    font-family:"Ubuntu",sans-serif;font-weight:500;text-align:center;padding-top:24px;line-height:28px}
  .front-header .line1{font-size:21px}
  .front-header .line2{font-size:21px;font-weight:700}
  .front-photo{left:0;top:103px;width:540px;height:240px;
    background:linear-gradient(135deg,#c9d2da 0%,#5c6a78 35%,#9fb0bf 55%,#2f3944 80%,#7e8d9a 100%)}
  .front-tag{left:16px;top:296px;color:var(--white);font-family:"Ubuntu",sans-serif}
  .front-tag h2{font-size:17px;font-weight:500;letter-spacing:.3px}
  .front-tag p{font-size:10px;font-weight:700;line-height:13px;margin-top:5px}
  .brand{display:flex;align-items:center;gap:6px;font-family:"Ubuntu",sans-serif;font-weight:500}
  .brand .mark{width:34px;height:34px;background:var(--white)}
  .brand--front{left:385px;top:262px;color:var(--white);font-size:22px}
  .intro{left:15px;top:374px;width:210px;font-size:8.1px;line-height:11.3px;text-align:justify}
  .checks{list-style:none;margin:9px 0}
  .checks li{position:relative;padding-left:14px;margin-bottom:7px;text-align:left}
  .checks li::before{content:"";position:absolute;left:1px;top:2px;width:6px;height:3px;border-left:1.4px solid var(--orange);border-bottom:1.4px solid var(--orange);transform:rotate(-45deg)}
  .panel{left:245px;top:388px;width:285px;color:var(--white);font-size:7.1px;line-height:9.6px}
  .panel h3{font-size:9.4px;font-weight:700;text-decoration:underline;margin:0 0 7px}
  .panel ul{list-style:none;margin-bottom:8px}
  .panel li{position:relative;padding-left:11px;margin-bottom:9px}
  .panel li::before{content:"";position:absolute;left:2px;top:3px;width:4px;height:4px;border-radius:50%;background:var(--white)}
  .front-phone{left:18px;top:733px;color:var(--white);font-size:13px;font-weight:600;font-family:"Ubuntu",sans-serif;display:flex;align-items:center;gap:4px}
  .front-web{right:14px;top:722px;color:var(--white);font-family:"Ubuntu",sans-serif;font-weight:500;font-size:19px}

  /* back */
  .back-photo{left:282px;top:73px;width:246px;height:408px;
    background:radial-gradient(circle at 45% 38%,#fffdf4 0%,#e8dcc0 18%,#8d8068 45%,#4a4136 75%,#2e2822 100%)}
  .back-intro{left:19px;top:132px;width:247px}
  .back-intro h2{color:var(--teal-dark);font-family:"Ubuntu",sans-serif;font-weight:700;font-size:19.5px;line-height:26px;text-align:justify;text-align-last:left}
  .back-intro p{font-size:13.6px;line-height:19px;text-align:justify;margin-top:2px}
  .brand--back{left:20px;top:534px;color:var(--ink);font-size:32px;font-weight:500}
  .brand--back .mark{width:38px;height:38px;background:var(--orange)}
  .more{left:290px;top:496px;width:240px}
  .more h2{font-family:"Roboto Condensed",sans-serif;font-weight:700;font-size:34px;color:var(--teal-dark);letter-spacing:.3px}
  .more p{font-size:11.5px;margin-top:6px}
  .more .web{font-size:15.5px;margin-top:4px;display:flex;align-items:center;gap:6px}
  .dot{width:9px;height:9px;border-radius:50%;background:var(--orange);display:inline-block}
  .back-call{left:26px;top:668px;color:var(--white);font-family:"Ubuntu",sans-serif}
  .back-call .label{font-size:22px;font-weight:500}
  .back-call .number{font-size:31px;font-weight:500;display:flex;align-items:center;gap:4px;margin-top:6px}
  .back-mail{right:14px;top:663px;color:var(--white);font-family:"Ubuntu",sans-serif;font-weight:500;font-size:19px;display:flex;align-items:center;gap:8px}
</style>
</head>
<body>
<div class="canvas">

  <!-- Front side -->
  <section class="flyer flyer--front">
    <div class="abs front-header">
      <div class="line1">Ontzorging van uw project delivery:</div>
      <div class="line2">PROJECT MANAGEMENT AS A SERVICE (PMAAS)</div>
    </div>
    <div class="abs front-photo" role="img" aria-label="Close-up photo of polished steel gears and machinery"></div>
    <svg class="shapes" viewBox="0 0 540 758" aria-hidden="true">
      <polygon points="0,267 300,267 236,362 0,362" fill="var(--teal)"/>
      <polygon points="300,268 540,212 540,372 236,362" fill="var(--orange)"/>
      <polygon points="236,372 440,330 540,355 540,668 236,732" fill="var(--teal)"/>
      <polygon points="180,758 540,676 540,758" fill="var(--orange)"/>
      <polygon points="0,720 236,738 190,758 0,758" fill="var(--teal)"/>
    </svg>
    <div class="abs front-tag">
      <h2>VELTORIS</h2>
      <p>FOR A DIFFERENT APPROACH IN<br>BUSINESS IMPROVEMENT</p>
    </div>
    <div class="abs brand brand--front"><span class="mark"></span>veltoris</div>

    <div class="abs intro">
      <p>U kunt voor de realisatie van uw projectportfolio de hulp inroepen van externe projectmanagers, en daarbij zelf de coördinatie verzorgen. Grote kans dat u dan tegen één of meer van de volgende zaken aan loopt:</p>
      <ul class="checks">
        <li>Een wisselende kwaliteit van projectmanagers</li>
        <li>Problemen om kosten inzichtelijk en voorspelbaar of beheersbaar houden (management rapportage)</li>
        <li>Een ad hoc relatie met uw projectmanagers en leveranciers</li>
        <li>Beperkt leergedrag en herhaling van fouten</li>
        <li>Tijdverlies en kosten omdat u veel tijd kwijt bent aan uitleg van rand voorwaardelijke zaken</li>
      </ul>
      <p>Een alternatief is onze PMAAS-service. Die bevat alle ingrediënten om uw projectenportfolio kostenefficiënt en op hoog kwaliteitsniveau te realiseren. Veltoris zorgt voor inzet van projectmanagers die al 'up to speed' zijn als ze bij u binnenkomen. Ze hebben de juiste expertise, zijn al ingewerkt op uw of onze standaard methodiek en op uw organisatorische setting. En heeft u ineens meer of minder werk? Geen probleem. Dan schalen wij net zo gemakkelijk op en af.</p>
    </div>

    <div class="abs panel">
      <h3>Wij zorgen voor</h3>
      <ul>
        <li>een eenduidige werkwijze, rapportering en gebruik van tooling</li>
        <li>een scherpe intake en voorbereidingsfase van de te starten projecten</li>
        <li>de benodigde op-enafschaling van project managers met het juiste profiel</li>
        <li>ingewerkte projectmanagers op de overeengekomen projectmethode</li>
        <li>continue monitoring op afgesproken KPI's over de projecten heen</li>
        <li>periodiek overleg over de performance</li>
        <li>continue verbetering op basis van klantevaluaties</li>
        <li>facturatie volgens afspraak (milestone-based)</li>
      </ul>
      <h3>U zorgt voor:</h3>
      <ul>
        <li>een up to date forecast van de te realiseren projectportfolio</li>
        <li>een goede projectbrief als basis voor onze intake</li>
      </ul>
      <h3>PMO en PPM</h3>
      <p>Wilt u zich nog meer laten ontzorgen? Dat kan! Naast onze PMAAS-service leveren wij ook diensten op het gebied van Project Management Office (PMO) en/of Project Portfolio Management (PPM). Wij kunnen deze activiteiten voor u opzetten, maar ook de operationele aansturing ervan ondersteunen of voor onze rekening nemen.</p>
    </div>

    <div class="abs front-phone">
      <svg width="11" height="12" viewBox="0 0 24 24" aria-hidden="true"><path fill="var(--white)" d="M6.6 10.8a15.1 15.1 0 0 0 6.6 6.6l2.2-2.2a1 1 0 0 1 1-.25 11.4 11.4 0 0 0 3.6.57 1 1 0 0 1 1 1V20a1 1 0 0 1-1 1A17 17 0 0 1 3 4a1 1 0 0 1 1-1h3.5a1 1 0 0 1 1 1c0 1.25.2 2.45.57 3.57a1 1 0 0 1-.25 1z"/></svg>
      085 - 0047312
    </div>
    <div class="abs front-web">www.veltoris.com</div>
  </section>

  <!-- Back side -->
  <section class="flyer flyer--back">
    <div class="abs back-photo" role="img" aria-label="Photo of a glowing light bulb among unlit bulbs"></div>
    <svg class="shapes" viewBox="0 0 540 758" aria-hidden="true">
      <polygon points="0,0 285,0 245,53 0,105" fill="var(--orange)"/>
      <polygon points="120,0 285,0 245,53" fill="var(--orange)"/>
      <polygon points="285,0 540,0 540,103 245,53" fill="var(--teal)"/>
      <polygon points="0,633 540,703 540,758 0,758" fill="var(--teal)"/>
      <polygon points="200,670 540,597 540,740" fill="var(--orange)"/>
    </svg>
    <div class="abs back-intro">
      <h2>Veltoris: innovatief in verandertrajecten</h2>
      <p>Als management consultancy bureau houden wij ons bezig met de begeleiding van veranderingen in bedrijven. Op het gebied van strategie, maar ook van processen en systemen. Wij onderscheiden ons door toepassing van visualisatie technieken, bedrijfsproces simulaties en unieke services en zijn continu op zoek naar nieuwe toepassingsmogelijkheden op dit gebied. Door de krachten van uw medewerkers en die van ons te verenigen, komen we tot betere en snellere resultaten. Daarbij gaan wij samen op reis. Want veranderingen kun je niet leren, je moet ze ervaren.</p>
    </div>
    <div class="abs brand brand--back"><span class="mark"></span>veltoris</div>
    <div class="abs more">
      <h2>MEER WETEN</h2>
      <p>Wilt u meer weten, bekijk onze website:</p>
      <div class="web"><span class="dot"></span>www.veltoris.com</div>
    </div>
    <div class="abs back-call">
      <div class="label">Call Us At</div>
      <div class="number">
        <svg width="24" height="26" viewBox="0 0 24 24" aria-hidden="true"><path fill="var(--white)" d="M6.6 10.8a15.1 15.1 0 0 0 6.6 6.6l2.2-2.2a1 1 0 0 1 1-.25 11.4 11.4 0 0 0 3.6.57 1 1 0 0 1 1 1V20a1 1 0 0 1-1 1A17 17 0 0 1 3 4a1 1 0 0 1 1-1h3.5a1 1 0 0 1 1 1c0 1.25.2 2.45.57 3.57a1 1 0 0 1-.25 1z"/></svg>
        085 - 0047312
      </div>
    </div>
    <div class="abs back-mail">
      <svg width="14" height="10" viewBox="0 0 14 10" aria-hidden="true"><rect x=".5" y=".5" width="13" height="9" fill="none" stroke="var(--white)"/><polyline points=".5,.5 7,6 13.5,.5" fill="none" stroke="var(--white)"/></svg>
      info@veltoris.com
    </div>
  </section>

</div>
</body>
</html>
```